WE are a specialised tutoring business looking to a have a landing page design

we need a landing page designed for our business. We provide specialised tutoring for children with learning difficulties. I have attached a brief which includes our logo and also the content for the page.

Target Market(s)

parents

Number of Pages Required

1 page

Requirements
Must have
• our existing logo and the content provided

```html
<!DOCTYPE html>
<html lang="en">
<head>
<meta charset="utf-8">
<title>thebrightpath – Specialised learning for Children</title>
<link rel="stylesheet" href="https://fonts.googleapis.com/css2?family=Noto+Serif&family=Work+Sans:wght@400;500&family=Montserrat:wght@400;700&family=Libre+Baskerville&display=swap">
<style>
:root{
  --green:#13a70f;
  --green-ring:#1fb81a;
  --ink:#111;
  --muted:#555;
  --panel:#f2f2f2;
  --white:#fff;
}
*{margin:0;padding:0;box-sizing:border-box}
html,body{width:794px;height:1200px;overflow:hidden;background:var(--white)}
body{position:relative;font-family:'Montserrat',sans-serif;color:var(--ink)}

.hero{position:absolute;left:0;top:0;width:794px;height:434px}
.hero-photo{position:absolute;inset:0;background:
  radial-gradient(ellipse at 35% 30%,#a65a5f 0,#7d4c52 18%,transparent 40%),
  linear-gradient(180deg,#6e6a6b 0%,#8f8b8c 45%,#9d9a9b 75%,#6d6a6b 100%)}
.hero-shade{position:absolute;inset:0;background:linear-gradient(90deg,rgba(0,0,0,.05),rgba(0,0,0,.25))}
.brand{position:absolute;left:0;width:794px;top:42px;display:flex;justify-content:center;align-items:center;gap:6px}
.brand-dot{width:12px;height:12px;border-radius:50%;background:var(--green)}
.brand-name{font-family:'Noto Serif',serif;font-size:19px;color:#7cc242}
.hero-copy{position:absolute;left:450px;top:155px;width:300px;color:var(--white)}
.hero-title{font-family:'Noto Serif',serif;font-weight:400;font-size:29px;line-height:36px;margin-bottom:10px}
.hero-text{font-family:'Work Sans',sans-serif;font-weight:500;font-size:13px;line-height:16.3px}

.features{position:absolute;left:0;top:434px;width:794px;height:342px;background:var(--panel)}
.feature{position:absolute;top:44px;width:210px}
.feature-icon{width:52px;height:52px;border-radius:50%;border:3px solid var(--green-ring);display:flex;align-items:center;justify-content:center;margin-bottom:22px}
.feature-title{font-size:17.5px;font-weight:700;margin-bottom:14px;white-space:nowrap}
.feature-text{font-size:9.2px;line-height:16.3px}

.cta{position:absolute;left:0;top:776px;width:794px;height:204px;background:
  linear-gradient(180deg,#2b2a29 0%,#262625 45%,#1f3320 65%,#2c3a2d 100%)}
.cta-title{position:absolute;top:58px;width:794px;text-align:center;color:var(--white);font-size:16px;font-weight:700;letter-spacing:.3px}
.field{position:absolute;top:99px;width:204px;height:37px;border:1.5px solid var(--white);color:var(--white);font-size:15px;padding:9px 24px;font-family:'Montserrat',sans-serif}
.send{position:absolute;top:99px;left:575px;width:87px;height:37px;background:var(--green);color:var(--white);font-weight:700;font-size:14.5px;letter-spacing:.5px;display:flex;align-items:center;justify-content:center}

.contact{position:absolute;left:53px;top:1040px}
.contact-title{font-family:'Libre Baskerville',serif;font-size:17px;font-weight:400;margin-bottom:20px}
.contact-line{font-family:'Work Sans',sans-serif;font-size:12px;margin-bottom:7px;color:var(--ink)}
.contact-line span{color:var(--muted);margin-left:6px}
.social{position:absolute;left:574px;top:1058px;display:flex;gap:12px}
.social i{width:33px;height:33px;border-radius:50%;border:2px solid var(--ink)}
.footer{position:absolute;top:1169px;width:794px;text-align:center;font-family:'Work Sans',sans-serif;font-size:9.5px}
</style>
</head>
<body>
<header class="hero">
  <div class="hero-photo" role="img" aria-label="Photo of a young girl with a red headband writing at a table in a classroom"></div>
  <div class="hero-shade"></div>
  <div class="brand"><span class="brand-dot"></span><span class="brand-name">thebrightpath</span></div>
  <div class="hero-copy">
    <h1 class="hero-title">Specialised learning for Children</h1>
    <p class="hero-text">thebrightpath is a team of psychologists and teachers focused on supporting children with social, emotional, and learning difficulties. We provide specialised tutoring and support for children and their families</p>
  </div>
</header>

<section class="features">
  <article class="feature" style="left:75px">
    <div class="feature-icon" style="margin-left:38px">
      <svg width="26" height="26" viewBox="0 0 26 26" fill="none" stroke="#111" stroke-width="1.4" stroke-linecap="round"><path d="M9 15c-2-2-2.5-4-1.5-6a5.5 5.5 0 0 1 11 0c1 2 .5 4-1.5 6v3H9z"/><path d="M10 21h6M11 23.5h4M13 1.5v2M4 6l1.5 1M22 6l-1.5 1M2.5 12h2M21.5 12h2"/></svg>
    </div>
    <h2 class="feature-title">Know the Child</h2>
    <p class="feature-text">We are dedicated to evidence-based assessment and diagnosis. We believe that early intervention requires a clear understanding of the unique challenges faced by the child. This involves assessment and also a dedication to working with children, their parents, and also their preschool and school contexts. This allows us to ensure that any intervention is tailored to the child.</p>
  </article>
  <article class="feature" style="left:305px">
    <div class="feature-icon" style="margin-left:36px">
      <svg width="28" height="26" viewBox="0 0 28 26" fill="none" stroke="#111" stroke-width="1.4" stroke-linecap="round"><path d="M15 14V3M15 7c-2-1-3-3-3-4M15 6c2-1 3-2.5 3-3.5M15 10c-2-.5-3.5-2-3.5-3M15 10c2-.5 3.5-2 3.5-3"/><path d="M3 17h6c2 0 4 1 5 2h6l5-3c1 0 1.5 1 .5 2l-6 4H9l-6-1z" fill="#111"/></svg>
    </div>
    <h2 class="feature-title">Meet the Need</h2>
    <p class="feature-text">We provide individualised tutoring for children that focuses on their specific areas of learning need. Our team are dedicated to providing best-practice learning support within an environment of encouragement and care, understanding the impact that learning difficulties can have on broader areas of confidence and self-concept.</p>
  </article>
  <article class="feature" style="left:531px">
    <div class="feature-icon" style="margin-left:44px">
      <svg width="26" height="28" viewBox="0 0 26 28" fill="none" stroke="#111" stroke-width="1.4" stroke-linecap="round"><path d="M13 27V6M13 18c-3-1-6-4-7-7M13 14c3-1 6-3 7-6M13 22c2-1 4-2 5-4"/><ellipse cx="13" cy="4" rx="1.6" ry="3" fill="#111"/><ellipse cx="5" cy="9" rx="1.6" ry="3" fill="#111" transform="rotate(-40 5 9)"/><ellipse cx="21" cy="6" rx="1.6" ry="3" fill="#111" transform="rotate(40 21 6)"/><ellipse cx="19" cy="16" rx="1.5" ry="2.6" fill="#111" transform="rotate(60 19 16)"/></svg>
    </div>
    <h2 class="feature-title">Watch them Grow</h2>
    <p class="feature-text">We are committed to seeing growth, this requiring strategic intervention and the ability to assess and provide evidence of achievement. Our passion is not only to provide effective support, but also to help children and their families to see this growth, fostering a culture of positivity and engagement in learning</p>
  </article>
</section>

<section class="cta" role="img" aria-label="Dimmed photo of a student reading in a classroom">
  <h2 class="cta-title">GET TO KNOW MORE?</h2>
  <div class="field" style="left:129px">Your Email</div>
  <div class="field" style="left:351px">Phone Number</div>
  <div class="send">SEND</div>
</section>

<section class="contact">
  <h2 class="contact-title">CONTACT US</h2>
  <p class="contact-line">Address: <span>12/48 Harbour View Road, Lindfield, 2070</span></p>
  <p class="contact-line">Email: <span>info@thebrightpath.com.au</span></p>
</section>
<div class="social" aria-label="Social links"><i></i><i></i><i></i><i></i></div>

<footer class="footer">© 2019.</footer>
</body>
</html>
```